Website for a web design agency

We are a website and marketing agency. We do website design, development, and well as Brindle and Quorvia advertising and analytics. We ourselves need a new website for our own brand. We are working on some designs in-house with our own designers, but we also wanted to see what outside designers would come up with.
We are starting off with the homepage, and here is the breakdown of the sections:
https://files.brindlework.example/sheet/d/7kqTr2VnPLwXeHsaMcY4oBfJzuGNtKdWiEh3Rx9pLmQb/view?mode=share
This doc also has many links to sites we have done, which you can take screenshots of for the portfolio section.
In terms of the "look" I am going for, I want to look high-end and very beautiful designs. I found this website that I like a lot that you can use some of the elements of, just as a starting point:
http://velmarkstudio.example/layouts/pixelbarn/html/ostrevo/index.html and here is another design option they have http://velmarkstudio.example/layouts/pixelbarn/html/ostrevo/index-4.html
I'm also uploading my logo. The logo matches the gold and black look from these websites, but I would be open to switching to another color scheme if needed.
This is the link to my very old website, which you can use for some of the dummy text, and a pic of myself. I will be taking more pics of myself:
https://theplumtreeandwillowgroup.example/
We need a homepage and a portfolio page right now, but if you are the winner, we will be hiring you to make additional pages.
Updates
More designs continue to come in even today, and I want to make sure no other designers are still submitting designs.
Target Market(s)
medium and large businesses owners, and non-profits
Number of Pages Required
1 page

```html
<!DOCTYPE html>
<html lang="en">
<head>
<meta charset="utf-8">
<title>Halvern Strategies — Website Development and Online Marketing</title>
<link rel="stylesheet" href="https://fonts.googleapis.com/css2?family=Oswald:wght@500;600;700&family=Montserrat:wght@500;600;700;800&family=Open+Sans:wght@400;600;700&display=swap">
<style>
:root{
  --gold:#f4b719;
  --gold-deep:#e2a40c;
  --ink:#1c1c1c;
  --night:#232323;
  --charcoal:#2e2e2e;
  --slate:#3a3a3a;
  --paper:#ffffff;
  --mist:#f3f3f3;
  --text:#555555;
  --muted:#9a9a9a;
  --head:'Montserrat',sans-serif;
  --display:'Oswald',sans-serif;
  --body:'Open Sans',sans-serif;
}
*{box-sizing:border-box;margin:0;padding:0}
html,body{width:1200px;height:5060px;overflow:hidden}
body{position:relative;background:var(--paper);font-family:var(--body);color:var(--text)}
.abs{position:absolute}
.fill{position:absolute}

/* hero */
.hero{position:absolute;left:0;top:0;width:1200px;height:560px;overflow:hidden;
  background:linear-gradient(90deg,#1a1a1a 0%,#2b2b2b 40%,#4a4540 70%,#2a2826 100%)}
.hero-photo{left:470px;top:0;width:520px;height:560px;
  background:radial-gradient(ellipse at 50% 40%,#8a6a55 0%,#5b463a 35%,#3a3330 65%,rgba(40,38,36,0) 85%)}
.brand{left:68px;top:16px;font-family:var(--head);font-weight:800;font-size:26px;color:var(--paper);letter-spacing:1px;display:flex;align-items:center;gap:10px}
.brand-dot{width:12px;height:12px;background:var(--gold)}
.brand-tag{left:90px;top:48px;font-family:var(--head);font-weight:700;font-size:10px;letter-spacing:3px;color:var(--paper)}
.top-contact{right:60px;top:18px;font-size:12px;color:var(--paper);display:flex;gap:18px}
.top-contact b{color:var(--gold);font-weight:600}
.social-rail{right:52px;top:150px;display:flex;flex-direction:column;gap:24px}
.social-rail span{width:14px;height:14px;border-radius:50%;background:var(--paper);opacity:.85}
.hero-title{left:68px;top:170px;font-family:var(--display);font-weight:700;font-size:90px;line-height:.98;color:var(--paper);letter-spacing:1px}
.hero-sub{left:68px;top:376px;font-family:var(--head);font-weight:600;font-size:19px;color:var(--paper)}
.hero-sub em{font-style:normal;color:var(--gold)}
.btn-ghost{left:68px;top:420px;border:1px solid var(--paper);color:var(--paper);font-size:11px;font-weight:600;letter-spacing:1px;padding:12px 20px}

/* welcome */
.welcome{position:absolute;left:0;top:560px;width:1200px;height:400px}
.device-shot{left:100px;top:50px;width:490px;height:314px;
  background:linear-gradient(135deg,#2a1c6e 0%,#5b2fb3 45%,#8f4fe0 70%,#3b2a8a 100%)}
.welcome-kicker{left:812px;top:96px;font-size:11px;color:var(--muted);letter-spacing:1px}
.welcome-title{left:812px;top:114px;font-family:var(--head);font-weight:800;font-size:34px;color:var(--ink);line-height:1.05}
.welcome-text{left:812px;top:196px;width:330px;font-size:13px;line-height:1.55}

/* section titles */
.sec-title{left:0;width:1200px;text-align:center;font-family:var(--head);font-weight:800;font-size:40px;color:var(--ink)}
.sec-sub{left:300px;width:600px;text-align:center;font-size:12px;line-height:1.6;color:var(--muted)}

/* services */
.service{position:absolute;width:344px}
.service .shot{height:260px;width:344px}
.service h3{margin-top:14px;text-align:center;font-family:var(--head);font-weight:700;font-size:15px;color:var(--ink);letter-spacing:.5px}

/* case studies */
.cases{position:absolute;left:0;top:1840px;width:1200px;height:900px;
  background:linear-gradient(160deg,#2a2a2a 0%,#1f1f1f 50%,#2a2826 100%)}
.cases-title{left:68px;top:100px;font-family:var(--head);font-weight:700;font-size:36px;color:var(--paper)}
.cases-text{left:68px;top:150px;width:470px;font-size:12px;line-height:1.6;color:#bdbdbd}
.case-card{position:absolute;padding:26px 24px;color:var(--paper)}
.case-card h4{font-family:var(--head);font-weight:700;font-size:15px;letter-spacing:.5px}
.case-card p{margin-top:10px;font-size:11.5px;line-height:1.6;color:#c9c9c9}
.case-card .more{display:inline-block;margin-top:16px;font-size:10px;font-weight:700;letter-spacing:1px;background:#4a4a4a;padding:8px 14px}

/* team */
.member{position:absolute;top:2880px;width:248px}
.member .portrait{width:248px;height:240px}
.member h4{margin-top:14px;font-family:var(--head);font-weight:700;font-size:12px;color:var(--ink);letter-spacing:.5px}
.member span{display:block;font-size:10px;color:var(--muted);margin-top:2px}

/* testimonials */
.testi{position:absolute;left:0;top:3180px;width:1200px;height:360px;
  background:linear-gradient(90deg,#1c1c1c 0%,#2c2c2c 45%,#3a3733 100%)}
.testi-kicker{left:68px;top:60px;font-size:11px;color:#cfcfcf;letter-spacing:1px}
.testi-title{left:68px;top:76px;font-family:var(--head);font-weight:700;font-size:34px;color:var(--paper)}
.testi-text{left:68px;top:124px;width:300px;font-size:11.5px;line-height:1.6;color:#bdbdbd}
.quote{position:absolute;top:100px;width:300px;height:230px;background:var(--paper);padding:70px 22px 20px;box-shadow:0 6px 20px rgba(0,0,0,.25)}
.quote .avatar{position:absolute;left:126px;top:-26px;width:48px;height:48px;border-radius:50%;background:linear-gradient(135deg,#b38b6d,#6b5243);border:3px solid var(--paper)}
.quote p{font-size:11px;line-height:1.65;color:var(--text)}
.quote b{display:block;margin-top:14px;font-family:var(--head);font-size:11px;color:var(--ink)}

/* portfolio */
.work{position:absolute}
.work-caption{position:absolute;left:0;bottom:0;width:100%;background:rgba(28,28,28,.85);padding:12px 16px}
.work-caption h5{font-family:var(--head);font-weight:700;font-size:12px;color:var(--gold)}
.work-caption p{font-size:10px;color:#d0d0d0;margin-top:4px}

/* audit */
.audit{position:absolute;left:0;top:4340px;width:1200px;height:420px;
  background:linear-gradient(120deg,var(--gold) 0%,#f7c63e 50%,var(--gold-deep) 100%)}
.audit-photo{left:700px;top:20px;width:400px;height:400px;background:linear-gradient(160deg,#e9d2b8 0%,#c79a3a 55%,rgba(226,164,12,0) 100%)}
.audit-card{left:68px;top:210px;width:580px;height:190px;background:var(--paper);padding:28px 34px;box-shadow:0 8px 24px rgba(0,0,0,.15)}
.audit-card small{font-size:10px;color:var(--muted);letter-spacing:1px}
.audit-card h3{font-family:var(--head);font-weight:800;font-size:30px;line-height:1.05;color:var(--ink);margin-top:4px}
.audit-form{display:flex;margin-top:18px}
.audit-form span{flex:0 0 380px;height:36px;border:1px solid #d6d6d6;font-size:11px;color:var(--muted);padding:10px 12px}
.audit-form b{flex:0 0 112px;height:36px;background:var(--gold);color:var(--ink);font-size:10px;font-weight:700;letter-spacing:1px;text-align:center;line-height:36px}

/* footer */
.footer{position:absolute;left:0;top:4760px;width:1200px;height:300px;background:var(--ink)}
.footer-photo{left:0;top:0;width:250px;height:300px;background:linear-gradient(180deg,#4b4038 0%,#2e2926 100%)}
.footer-tab{left:238px;top:40px;width:30px;height:160px;background:var(--gold)}
.foot-col{position:absolute;top:36px}
.foot-col h6{font-family:var(--head);font-weight:700;font-size:12px;color:var(--paper);letter-spacing:1px}
.foot-col i{display:block;width:24px;height:2px;background:var(--gold);margin:8px 0 14px}
.foot-col li{list-style:none;font-size:11px;color:#a9a9a9;line-height:22px;display:flex;align-items:center;gap:8px}
.foot-col li .ico{width:10px;height:10px}
.foot-col li .dot{width:20px;height:20px;border-radius:50%;background:#3b3b3b;flex:none}
.foot-col li .dot.on{background:#3b5bd6}
.copyright{left:250px;width:950px;top:272px;text-align:center;font-size:10px;color:#8a8a8a}
.copyright b{color:var(--gold)}
</style>
</head>
<body>

<!-- hero -->
<section class="hero">
  <div class="fill hero-photo" role="img" aria-label="Portrait of the agency founder in a bright office"></div>
  <div class="abs brand"><span class="brand-dot"></span>HALVERN</div>
  <div class="abs brand-tag">STRATEGIES</div>
  <div class="abs top-contact"><b>555-0148-2290</b><span>hello@halvernstrategies.example</span></div>
  <div class="abs social-rail"><span></span><span></span><span></span><span></span></div>
  <h1 class="abs hero-title">WE<br>BUILD VALUE</h1>
  <p class="abs hero-sub">Enterprise Level Website Development <em>and</em> Online Marketing</p>
  <div class="abs btn-ghost">SEE HOW WE DO IT</div>
</section>

<!-- welcome -->
<section class="welcome">
  <svg class="abs" style="left:0;top:0" width="1200" height="400" viewBox="0 0 1200 400">
    <polygon points="0,0 760,0 0,110" fill="#f4b719"/>
    <polygon points="1200,170 1200,0 1100,0" fill="#232323"/>
    <polygon points="0,300 0,400 880,400" fill="#f4b719"/>
    <polygon points="1200,250 1200,400 760,400" fill="#f4b719"/>
  </svg>
  <div class="abs device-shot" role="img" aria-label="Laptop showing a quality assurance illustration"></div>
  <p class="abs welcome-kicker">WELCOME TO</p>
  <h2 class="abs welcome-title">HALVERN<br>STRATEGIES</h2>
  <p class="abs welcome-text">We are a website and marketing agency. We do website design, development, and well as Brindle and Quorvia advertising and analytics.</p>
</section>

<!-- what we do -->
<h2 class="abs sec-title" style="top:1010px">WHAT WE DO</h2>
<div class="service" style="left:68px;top:1200px">
  <div class="shot" role="img" aria-label="Website design on a yellow desk" style="background:linear-gradient(135deg,#f6c43a,#e7a914)"></div>
  <h3>WEBSITES</h3>
</div>
<div class="service" style="left:428px;top:1200px">
  <div class="shot" role="img" aria-label="Digital marketing landing page flyer" style="background:linear-gradient(135deg,#e56a2a,#2b2b2b)"></div>
  <h3>LANDING PAGES</h3>
</div>
<div class="service" style="left:788px;top:1200px">
  <div class="shot" role="img" aria-label="Person at a computer viewing a donation page" style="background:linear-gradient(135deg,#e8ddd2,#b9a08a)"></div>
  <h3>DONATION PAGES</h3>
</div>
<div class="service" style="left:68px;top:1500px">
  <div class="shot" role="img" aria-label="Pay per click notes with a coffee cup" style="background:linear-gradient(135deg,#d9d9d9,#8a8a8a)"></div>
  <h3>PPC AND FUNNELS</h3>
</div>
<div class="service" style="left:428px;top:1500px">
  <div class="shot" role="img" aria-label="Hands framing a sunset for video" style="background:linear-gradient(135deg,#3d3f5a,#c58a6a)"></div>
  <h3>VIDEO MARKETING</h3>
</div>
<div class="service" style="left:788px;top:1500px">
  <div class="shot" role="img" aria-label="Tablet with analytics graphics" style="background:linear-gradient(135deg,#1d1b3a,#5a3ea8)"></div>
  <h3>ANALYTICS AND OPTIMIZATION</h3>
</div>

<!-- case studies -->
<section class="cases">
  <h2 class="abs cases-title">CASE STUDIES</h2>
  <p class="abs cases-text">Sed ut perspiciatis unde omnis iste natus error sit voluptatem accusantium doloremque laudantium, totam rem aperiam, eaque ipsa quae ab illo inventore veritatis et quasi architecto.</p>
  <div class="fill" role="img" aria-label="Woman working at a laptop in a cafe" style="left:600px;top:80px;width:540px;height:360px;background:linear-gradient(135deg,#8a7b6c,#d8cbbd)"></div>
  <div class="case-card" style="left:600px;top:80px;width:260px;height:190px;background:rgba(34,34,34,.9)">
    <h4>GREAT EXPLORER OF TRUTH</h4>
    <p>Nemo enim ipsam voluptatem quia voluptas sit aspernatur aut odit aut fugit.</p>
    <span class="more">READ MORE</span>
  </div>
  <div class="fill" role="img" aria-label="Laptop and plant on a white desk" style="left:68px;top:300px;width:532px;height:500px;background:linear-gradient(135deg,#f1f1f1,#bdbdbd)"></div>
  <div class="case-card" style="left:330px;top:450px;width:250px;height:200px;background:#2b2b2b">
    <h4>FINIBUS BONORUM</h4>
    <p>Sed ut perspiciatis unde omnis iste natus error sit voluptatem accusantium.</p>
    <span class="more">READ MORE</span>
  </div>
  <div class="fill" role="img" aria-label="Woman writing at a desk by a window" style="left:600px;top:440px;width:540px;height:360px;background:linear-gradient(135deg,#e4d8cc,#9c8677)"></div>
  <div class="case-card" style="left:850px;top:450px;width:250px;height:190px;background:#3a3a3a">
    <h4>CONSEQUUNTUR MAGNI</h4>
    <p>Neque porro quisquam est qui dolorem ipsum quia dolor sit amet.</p>
    <span class="more">READ MORE</span>
  </div>
</section>

<!-- team -->
<h2 class="abs sec-title" style="top:2770px">OUR TEAM</h2>
<p class="abs sec-sub" style="top:2824px">Sed ut perspiciatis unde omnis iste natus error sit voluptatem accusantium doloremque laudantium, totam rem aperiam eaque ipsa quae inventore.</p>
<div class="member" style="left:68px"><div class="portrait" role="img" aria-label="Team member portrait" style="background:linear-gradient(135deg,#d9d2c7,#8b7563)"></div><h4>OWEN MARLOWE</h4><span>Lead Developer</span></div>
<div class="member" style="left:340px"><div class="portrait" role="img" aria-label="Team member portrait" style="background:linear-gradient(135deg,#cfc6bd,#9c7f63)"></div><h4>TESSA BRIGHTWELL</h4><span>Marketing Director</span></div>
<div class="member" style="left:608px"><div class="portrait" role="img" aria-label="Team member portrait" style="background:linear-gradient(135deg,#ded9d3,#6b4f3d)"></div><h4>RAVI ODUYA</h4><span>Designer</span></div>
<div class="member" style="left:880px"><div class="portrait" role="img" aria-label="Team member portrait" style="background:linear-gradient(135deg,#e5d4c2,#b58b5d)"></div><h4>MIRA CASTELL</h4><span>Art Director</span></div>

<!-- testimonials -->
<section class="testi">
  <p class="abs testi-kicker">HAPPY CUSTOMER</p>
  <h2 class="abs testi-title">TESTIMONIALS</h2>
  <p class="abs testi-text">Sed ut perspiciatis unde omnis iste natus error sit voluptatem accusantium doloremque laudantium, totam rem aperiam eaque ipsa quae.</p>
  <div class="quote" style="left:470px">
    <div class="avatar" role="img" aria-label="Client portrait"></div>
    <p>Temporibus autem quibusdam et aut officiis debitis aut rerum necessitatibus saepe eveniet ut et voluptates repudiandae sint et molestiae non recusandae.</p>
    <b>D. ARLEN</b>
  </div>
  <div class="quote" style="left:800px;top:80px">
    <div class="avatar" role="img" aria-label="Client portrait"></div>
    <p>Temporibus autem quibusdam et aut officiis debitis aut rerum necessitatibus saepe eveniet ut et voluptates repudiandae sint et molestiae.</p>
    <b>L. VANCE</b>
  </div>
</section>

<!-- portfolio -->
<h2 class="abs sec-title" style="top:3600px">PORTFOLIO</h2>
<div class="work" role="img" aria-label="Donation page website screenshot" style="left:68px;top:3720px;width:344px;height:240px;background:linear-gradient(135deg,#2d3b55,#7a8aa6)">
  <div class="work-caption"><h5>DONATION PAGE</h5><p>A clean giving page built for a regional non-profit.</p></div>
</div>
<div class="work" role="img" aria-label="Video production company website screenshot" style="left:428px;top:3720px;width:344px;height:240px;background:linear-gradient(135deg,#0f2a5c,#2f5fb3)"></div>
<div class="work" role="img" aria-label="Healthcare website screenshot" style="left:788px;top:3720px;width:344px;height:240px;background:linear-gradient(135deg,#e6eef8,#3a5fa8)"></div>
<div class="work" role="img" aria-label="Children's charity website screenshot" style="left:68px;top:3990px;width:344px;height:300px;background:linear-gradient(135deg,#f4f0ea,#6fc2e6)"></div>
<div class="work" role="img" aria-label="Wellness coaching website screenshot" style="left:428px;top:3990px;width:704px;height:300px;background:linear-gradient(90deg,#faf6f2 0%,#f3e4dc 55%,#d4b293 100%)">
  <div class="abs" style="left:0;top:0;width:704px;height:30px;background:#1d2e6e"></div>
</div>

<!-- audit -->
<section class="audit">
  <svg class="abs" style="left:0;top:0" width="1200" height="420" viewBox="0 0 1200 420">
    <polygon points="0,0 520,0 0,180" fill="#f7c84a"/>
  </svg>
  <div class="abs audit-photo" role="img" aria-label="Smiling woman holding a laptop"></div>
  <div class="abs audit-card">
    <small>LET'S TALK</small>
    <h3>AUDIT AND<br>CONSULTATION</h3>
    <div class="audit-form"><span>Enter Your Email</span><b>SUBMIT NOW</b></div>
  </div>
</section>

<!-- footer -->
<footer class="footer">
  <div class="abs footer-photo" role="img" aria-label="Agency founder in a cap"></div>
  <div class="abs footer-tab"></div>
  <div class="foot-col" style="left:340px">
    <h6>SITEMAP</h6><i></i>
    <ul><li>Home</li><li>What We Do</li><li>Services</li><li>About Us</li><li>Team</li><li>Contact Us</li></ul>
  </div>
  <div class="foot-col" style="left:560px">
    <h6>WHAT WE DO</h6><i></i>
    <ul><li>Websites</li><li>Landing Pages</li><li>Donation Pages</li><li>PPC and Funnels</li><li>Video Marketing</li><li>Analytics and Insights</li></ul>
  </div>
  <div class="foot-col" style="left:780px">
    <h6>CONTACT US</h6><i></i>
    <ul>
      <li><svg class="ico" viewBox="0 0 10 10"><path d="M5 0a3.5 3.5 0 0 0-3.5 3.5C1.5 6 5 10 5 10s3.5-4 3.5-6.5A3.5 3.5 0 0 0 5 0z" fill="#f4b719"/></svg>120 Harbor Lane, Suite 4</li>
      <li><svg class="ico" viewBox="0 0 10 10"><path d="M2 0l2 2-1 1.5a6 6 0 0 0 3.5 3.5L8 6l2 2-1.5 2C4 10 0 6 0 1.5z" fill="#f4b719"/></svg>555-0148-2290</li>
      <li><svg class="ico" viewBox="0 0 10 10"><rect y="2" width="10" height="7" fill="#f4b719"/><path d="M0 2l5 4 5-4" stroke="#1c1c1c" fill="none"/></svg>hello@halvernstrategies.example</li>
    </ul>
  </div>
  <div class="foot-col" style="left:1010px">
    <h6>SOCIAL US</h6><i></i>
    <ul><li><span class="dot on"></span>Quorvia</li><li><span class="dot"></span>Chirpline</li><li><span class="dot"></span>Snapgrid</li></ul>
  </div>
  <p class="abs copyright">COPYRIGHT © 2024 <b>HALVERN STRATEGIES</b>. ALL RIGHTS RESERVED</p>
</footer>

</body>
</html>
```